Brochure design for healthcare software company

We need a tri-fold brochure design for our healthcare software company that provides software and services for clinicians who manage patients who have or may be diagnosed with cancer.

We have an existing web, business card design and trade show booth design and want the ultimate design to be consistent with these. All of the files including stock images are provided.

Target Market(s)

Nurses, Healthcare professionals

Industry/Entity Type

Healthcare

Requirements
Must have
• Design consistent with attached tradeshow booth and business card.

```html
<!DOCTYPE html>
<html lang="en">
<head>
<meta charset="utf-8">
<title>Tri-fold Brochure – Inside Spread</title>
<link href="https://fonts.googleapis.com/css2?family=Open+Sans:wght@400;600;700;800&display=swap" rel="stylesheet">
<style>
  :root {
    --stage: #e8eded;
    --paper: #ffffff;
    --paper-mid: #f1f2f4;
    --brand-blue: #1b5fe2;
    --brand-blue-light: #3a7cf0;
    --brand-green: #3fe04c;
    --brand-green-dark: #2fc43c;
    --charcoal: #494c50;
    --ink: #1e1f22;
  }
  * { box-sizing: border-box; margin: 0; padding: 0; }
  html, body { width: 1200px; height: 1200px; overflow: hidden; }
  body {
    background: var(--stage);
    font-family: "Open Sans", Arial, sans-serif;
    color: var(--ink);
  }
  .spread {
    position: absolute;
    left: 45px; top: 170px;
    width: 1110px; height: 860px;
    display: flex;
    box-shadow: 0 14px 40px rgba(0,0,0,.12);
  }
  .panel {
    position: relative;
    width: 370px; height: 860px;
    background: var(--paper);
    overflow: hidden;
  }
  .panel--middle { background: var(--paper-mid); }
  .band {
    position: absolute; left: 0; width: 100%;
    color: #fff; font-weight: 800; text-transform: uppercase;
    font-size: 21px; line-height: 1.35; letter-spacing: .2px;
    padding: 0 34px;
    display: flex; align-items: center;
  }
  .band--blue { background: var(--brand-blue); }
  .band--green { background: linear-gradient(90deg, var(--brand-green-dark), var(--brand-green)); }
  .band--charcoal { background: var(--charcoal); }
  .body-copy {
    position: absolute; left: 36px; right: 36px;
    font-size: 14px; line-height: 1.55; text-align: justify;
  }
  .media { position: absolute; }
  .secure-block {
    position: absolute; left: 0; right: 0; bottom: 0; height: 250px;
    background: linear-gradient(90deg, var(--brand-green-dark), var(--brand-green));
    clip-path: polygon(0 14%, 100% 0, 100% 100%, 0 100%);
    color: #fff; padding: 70px 36px 0;
  }
  .secure-block h2 { font-size: 21px; font-weight: 800; margin-bottom: 10px; }
  .secure-block p { font-size: 14px; line-height: 1.55; text-align: justify; }
</style>
</head>
<body>
<main class="spread">

  <!-- Left panel -->
  <section class="panel panel--left">
    <h2 class="band band--blue" style="top:0;height:110px;clip-path:polygon(0 0,100% 0,100% 78%,0 100%);padding-bottom:14px;">Simplified Navigation</h2>
    <p class="body-copy" style="top:125px;">Track all of your patients from their entry point, for example an abnormal screening exam or a positive diagnosis, through survivorship. Veraline Navigation allows you to easily maintain a record of all referrals, exams, treatments, contacts, appointments and notes for your patients.</p>
    <div class="media" role="img" aria-label="Photo of a smiling nurse on the phone at a desk with patient files"
         style="top:300px;left:30px;right:30px;height:270px;background:linear-gradient(135deg,#c9b9a4,#7d8aa0 55%,#3d6fc4);"></div>
    <h2 class="band band--green" style="top:560px;height:105px;clip-path:polygon(0 10%,100% 0,100% 100%,0 88%);">Advanced Workflow<br>Tools</h2>
    <p class="body-copy" style="top:685px;">View and manage your entire patient load in a single dynamic work list area. Completely customizable to match your workflow. Create checklists for every step of your workflow to maintain consistent patient care and monitoring.</p>
  </section>

  <!-- Middle panel -->
  <section class="panel panel--middle">
    <h2 class="band band--charcoal" style="top:0;height:130px;clip-path:polygon(0 0,100% 0,100% 80%,0 100%);padding-bottom:16px;">Reporting and<br>Analytics</h2>
    <div class="media" role="img" aria-label="Illustration of a tablet displaying bar and pie chart analytics"
         style="top:150px;left:50px;right:40px;height:170px;border-radius:8px;background:linear-gradient(160deg,#e6f0fb,#9cc3ee 55%,#2f7fd8);"></div>
    <p class="body-copy" style="top:340px;">Quickly demonstrate the value of your navigation efforts with deep analytics and reporting. View current and historical trends for any or all of your facilities and staff, including detailed reporting on work loads, time to care, patient barriers, referrals and appointments.</p>
    <h2 class="band band--blue" style="top:480px;height:80px;clip-path:polygon(0 16%,100% 0,100% 84%,0 100%);">Eliminate Paper</h2>
    <div class="media" role="img" aria-label="Photo of a thick stack of paper documents"
         style="top:560px;left:30px;right:30px;height:150px;background:linear-gradient(135deg,#3e4348,#8a8d90 60%,#e8e4dc);"></div>
    <p class="body-copy" style="top:725px;">Manage all of your paperwork and patient forms in one easy to use area. Automatically create document packets and auto fill forms for patients or referrals with a single click.</p>
  </section>

  <!-- Right panel -->
  <section class="panel panel--right">
    <div class="media" role="img" aria-label="Photo of hands typing on a laptop keyboard"
         style="top:40px;left:20px;right:0;height:280px;background:linear-gradient(135deg,#8a5a9e,#e8c9bd 40%,#cfd3d8);"></div>
    <h2 class="band band--blue" style="top:0;height:95px;clip-path:polygon(0 0,100% 0,100% 72%,0 100%);padding-bottom:12px;">Integrated</h2>
    <p class="body-copy" style="top:335px;">Reduce double data entry by integrating the systems you already have. Patients can be seamlessly added and updated without manual efforts.</p>
    <div class="media" role="img" aria-label="Illustration of a glowing padlock on a blue circuit background"
         style="top:445px;left:20px;right:0;height:220px;background:radial-gradient(circle at 45% 45%,#3fa2ff,#0b3a9e 45%,#061a4a);"></div>
    <div class="secure-block">
      <h2>Secure</h2>
      <p>Built from the ground up with security in mind, Veraline Navigation is completely HIPAA compliant. Rest assured that your, and your patients data is protected.</p>
    </div>
  </section>

</main>
</body>
</html>
```